Working Capital graphics

Our business advisory firm requires 9 images to be re-created and improved in the branding of our business.

The 9 images have been uploaded below and the colours and branding of the business can be found at the website www.thornwickadvisory.com.au

```html
<!DOCTYPE html>
<html lang="en">
<head>
<meta charset="utf-8">
<title>Inventories – Inventory Drivers</title>
<link rel="stylesheet" href="https://fonts.googleapis.com/css2?family=Montserrat:wght@500;600;700&display=swap">
<style>
  :root {
    --navy: #1b2a4f;
    --brand-blue: #22408a;
    --label-blue: #2a3f8f;
    --orange: #f39322;
    --connector: #a0a0a0;
    --caption-grey: #9a9a9a;
    --box-border: #b4b4b4;
    --white: #ffffff;
  }
  html, body {
    margin: 0;
    padding: 0;
    width: 1200px;
    height: 1134px;
    overflow: hidden;
    background: var(--white);
  }
  .driver-chart {
    display: block;
    width: 1200px;
    height: 1134px;
    font-family: "Montserrat", Arial, sans-serif;
  }
  .chart-title { fill: var(--navy); font-size: 38px; font-weight: 600; letter-spacing: 1px; }
  .hub-ring { fill: var(--white); stroke: var(--navy); stroke-width: 1.5; }
  .hub-core { fill: var(--navy); }
  .hub-label { fill: var(--white); font-size: 18px; font-weight: 500; letter-spacing: 0.5px; }
  .level-caption { fill: var(--caption-grey); font-size: 31px; font-weight: 600; letter-spacing: 1px; }
  .connector { fill: none; stroke: var(--connector); stroke-width: 2; }
  .group-bar { fill: var(--brand-blue); }
  .group-label { fill: var(--white); font-size: 22px; font-weight: 600; letter-spacing: 0.5px; }
  .badge-ring { fill: var(--white); stroke: var(--brand-blue); stroke-width: 1.5; }
  .badge-core { fill: var(--orange); }
  .badge-number { fill: var(--white); font-size: 38px; font-weight: 500; }
  .sub-box { fill: var(--white); stroke: var(--box-border); stroke-width: 2; }
  .sub-label { fill: var(--label-blue); font-size: 18.5px; font-weight: 700; letter-spacing: 0.3px; }
</style>
</head>
<body>
<svg class="driver-chart" viewBox="0 0 1264 1194.5" xmlns="http://www.w3.org/2000/svg" role="img" aria-label="Inventory drivers grouped into planning, procurement, fulfillment and product range">
  <text class="chart-title" x="632" y="122" text-anchor="middle">INVENTORIES</text>

  <!-- connectors -->
  <path class="connector" d="M632 340 V400"/>
  <path class="connector" d="M218 470 V420 Q218 400 238 400 H1026 Q1046 400 1046 420 V470"/>
  <path class="connector" d="M494 400 V470 M770 400 V470"/>
  <path class="connector" d="M218 580 V1040 Q218 1060 238 1060 H1026 Q1046 1060 1046 1040 V580"/>
  <path class="connector" d="M494 580 V1060 M770 580 V1060"/>

  <!-- hub -->
  <circle class="hub-ring" cx="632" cy="248" r="101"/>
  <circle class="hub-core" cx="632" cy="248" r="85"/>
  <text class="hub-label" x="632" y="244" text-anchor="middle">INVENTORY</text>
  <text class="hub-label" x="632" y="263" text-anchor="middle">DRIVERS</text>

  <rect x="480" y="360" width="304" height="40" fill="#fff"/>
  <path class="connector" d="M632 360 V400"/>
  <text class="level-caption" x="617" y="391" text-anchor="end">DRIVER</text>
  <text class="level-caption" x="647" y="391">GROUP</text>

  <!-- driver groups -->
  <g class="driver-group">
    <rect class="group-bar" x="90" y="512" width="257" height="68" rx="18"/>
    <text class="group-label" x="218" y="562" text-anchor="middle">PLANNING</text>
    <circle class="badge-ring" cx="218" cy="498" r="42"/>
    <circle class="badge-core" cx="218" cy="498" r="35"/>
    <text class="badge-number" x="218" y="512" text-anchor="middle">10</text>
  </g>
  <g class="driver-group">
    <rect class="group-bar" x="366" y="512" width="257" height="68" rx="18"/>
    <text class="group-label" x="494" y="562" text-anchor="middle">PROCUREMENT</text>
    <circle class="badge-ring" cx="494" cy="498" r="42"/>
    <circle class="badge-core" cx="494" cy="498" r="35"/>
    <text class="badge-number" x="494" y="512" text-anchor="middle">11</text>
  </g>
  <g class="driver-group">
    <rect class="group-bar" x="641" y="512" width="257" height="68" rx="18"/>
    <text class="group-label" x="770" y="562" text-anchor="middle">FULFILLMENT</text>
    <circle class="badge-ring" cx="770" cy="498" r="42"/>
    <circle class="badge-core" cx="770" cy="498" r="35"/>
    <text class="badge-number" x="770" y="512" text-anchor="middle">12</text>
  </g>
  <g class="driver-group">
    <rect class="group-bar" x="917" y="512" width="257" height="68" rx="18"/>
    <text class="group-label" x="1046" y="562" text-anchor="middle">PRODUCT RANGE</text>
    <circle class="badge-ring" cx="1046" cy="498" r="42"/>
    <circle class="badge-core" cx="1046" cy="498" r="35"/>
    <text class="badge-number" x="1046" y="512" text-anchor="middle">13</text>
  </g>

  <!-- planning sub-groups -->
  <rect class="sub-box" x="90" y="648" width="257" height="68" rx="18"/>
  <text class="sub-label" x="218" y="679" text-anchor="middle">DEMAND</text>
  <text class="sub-label" x="218" y="698" text-anchor="middle">VARIABILITY</text>
  <rect class="sub-box" x="91" y="751" width="257" height="68" rx="18"/>
  <text class="sub-label" x="219" y="782" text-anchor="middle">PLANNING</text>
  <text class="sub-label" x="219" y="801" text-anchor="middle">COLABORATION</text>
  <rect class="sub-box" x="91" y="854" width="257" height="68" rx="18"/>
  <text class="sub-label" x="219" y="885" text-anchor="middle">INFORMATION</text>
  <text class="sub-label" x="219" y="904" text-anchor="middle">AVAILABILITY</text>
  <rect class="sub-box" x="91" y="957" width="257" height="68" rx="18"/>
  <text class="sub-label" x="219" y="988" text-anchor="middle">INVENTORY</text>
  <text class="sub-label" x="219" y="1007" text-anchor="middle">TARGET SETTING</text>

  <!-- procurement sub-groups -->
  <rect class="sub-box" x="365" y="648" width="257" height="68" rx="18"/>
  <text class="sub-label" x="494" y="679" text-anchor="middle">ORDER</text>
  <text class="sub-label" x="494" y="698" text-anchor="middle">QUANTITIES</text>
  <rect class="sub-box" x="366" y="751" width="257" height="68" rx="18"/>
  <text class="sub-label" x="495" y="782" text-anchor="middle">SUPPLIER LEAD</text>
  <text class="sub-label" x="495" y="801" text-anchor="middle">TIME VARIABILITY</text>
  <rect class="sub-box" x="366" y="854" width="257" height="68" rx="18"/>
  <text class="sub-label" x="495" y="885" text-anchor="middle">SUPPLIER QUALITY</text>
  <text class="sub-label" x="495" y="904" text-anchor="middle">VARIABILITY</text>

  <!-- fulfillment sub-groups -->
  <rect class="sub-box" x="641" y="648" width="257" height="68" rx="18"/>
  <text class="sub-label" x="770" y="679" text-anchor="middle">CUSTOMER SERVICE</text>
  <text class="sub-label" x="770" y="698" text-anchor="middle">LEVELS</text>
  <rect class="sub-box" x="642" y="751" width="257" height="68" rx="18"/>
  <text class="sub-label" x="771" y="782" text-anchor="middle">NETWORK</text>
  <text class="sub-label" x="771" y="801" text-anchor="middle">STRUCTURE</text>
  <rect class="sub-box" x="642" y="854" width="257" height="68" rx="18"/>
  <text class="sub-label" x="771" y="885" text-anchor="middle">INVENTORY</text>
  <text class="sub-label" x="771" y="904" text-anchor="middle">POSTPONEMENT</text>

  <!-- product range sub-groups -->
  <rect class="sub-box" x="917" y="648" width="257" height="68" rx="18"/>
  <text class="sub-label" x="1046" y="679" text-anchor="middle">CUSTOMER</text>
  <text class="sub-label" x="1046" y="698" text-anchor="middle">INVENTORY NEEDS</text>
  <rect class="sub-box" x="918" y="751" width="257" height="68" rx="18"/>
  <text class="sub-label" x="1047" y="782" text-anchor="middle">PART</text>
  <text class="sub-label" x="1047" y="801" text-anchor="middle">STANDARDISATION</text>
  <rect class="sub-box" x="918" y="854" width="257" height="68" rx="18"/>
  <text class="sub-label" x="1047" y="885" text-anchor="middle">SKU</text>
  <text class="sub-label" x="1047" y="904" text-anchor="middle">PROLIFERATION</text>

  <text class="level-caption" x="632" y="1097" text-anchor="middle">SUB-GROUP</text>
</svg>
</body>
</html>
```